International Property Consultancy

Brief Overview:

I need a dynamic and well designed website that is easy to use and understand. It has to be unique and different to generic templates that most websites seem to be these days. PLEASE NO GENERIC TEMPLATES FROM THE INTERNET.

Our business has 10 years experience working on struggling international developments that we then work in-house for to turn around and brings bout success. We stay within a project often for long periods of time until success is achieved. We are unique in our approach and completely different to the standard routes to market for many developments. The site is for developers to see what we have done in regards to previous projects, as such we want to incorporate video into this site with a strong design aesthetic. There will be videos of the past projects we have worked on, which will act as case studies.

I like very simple but punchy websites, that people can navigate and understand very easily. Also a big fan of unique and well thought out design aesthetic.

Initial Site layout thoughts:

1) Homepage:
2) About Us
3) What we've done / Work
This part has the projects we have worked on (France, Portugal, London, Morocco). Each one will have some video content and photo images, but also would be good to have a succinct way to mention what we did and the successes in a clever and punchy way.

4) Contact Us

* This is just a guideline. Would be open to input and creative direction on your own part.

*More details and websites we like can be seen in the brief doc attached.

PLEASE VIEW THE WIREFRAME WORD DOC ATTACHED.

Here there are also some more examples to help:

Here are just a few examples of websites and what I like about them:

- www.velmoro.com (clean, nice geometric design aesthetic, good animation when loading and changing pages well thought out all though also coulee be considered a bit dull and basic after the initial homepage slide)
- https://www.farbridgehub.net (Clean site, quite clinical, lacks video content and doesn't engage greatly).
- https://ruskotile.com (minimal, and like how it mixes the design aesthetic more with video and photo content)

- https://www.amberquillworks.com (like the layout of this and how it displays the projects and work section)

- https://brisk.com (Good use of video content)

- https://loomfield.studio (minimal to the point and mixes design with video and animation etc...)

Here is another couple of cool websites that may help give you some direction: https://halvenquay.com www.brisk.com

Hi there, One of the things I thought would be good on the homepage is to add the logo with a 'digital landscape' before flicking down into a slide with video content of the projects... Just an idea but have posted some pics in the brief. We would get this animated for the site. But if you have better ideas, please do run with them. Thanks,

Target Market(s)

Property developers

Number of Pages Required

4 page

Font styles to use
Other font styles liked:
• Read brief

Requirements
Must have
• Needs to be clean, dynamic and easy to follow on desktop and mobile. We will use it as a kind of portfolio website so will need to embed video of past projects we have worked on.

Read brief in docs.
Nice to have
• Clean
Should not have
• Not be another generic template website.
Not have random property stock photos. (We are not a property agency).

```html
<!DOCTYPE html>
<html lang="en">
<head>
<meta charset="utf-8">
<title>Terravane — About</title>
<link href="https://fonts.googleapis.com/css2?family=Poppins:wght@400;500;600;700&family=Arimo:wght@400;500&display=swap" rel="stylesheet">
<style>
  :root {
    --ink: #111111;
    --body: #3b3b3b;
    --navy: #1d2a4a;
    --deep-navy: #0b2d5a;
    --sky: #0aa2f0;
    --amber: #ffb800;
    --rule: #e3e3e3;
    --overlay: rgba(22, 58, 70, 0.82);
  }
  * { box-sizing: border-box; margin: 0; padding: 0; }
  html, body { width: 1128px; height: 1200px; overflow: hidden; background: #ffffff; }
  body { position: relative; font-family: 'Poppins', sans-serif; color: var(--ink); }

  .site-header { position: absolute; left: 84px; right: 81px; top: 16px; height: 60px; }
  .brand { position: absolute; left: 0; top: 0; font-size: 42px; font-weight: 500; color: var(--navy); letter-spacing: -0.5px; line-height: 60px; }
  .main-nav { position: absolute; right: 0; top: 17px; display: flex; gap: 40px; }
  .main-nav a { font-size: 17px; font-weight: 600; color: var(--ink); text-decoration: none; line-height: 24px; }

  .about { position: absolute; left: 191px; top: 204px; width: 780px; }
  .about h1 { font-size: 52px; font-weight: 600; line-height: 66px; letter-spacing: 0.3px; margin-bottom: 16px; }
  .about p { font-size: 20.5px; line-height: 32.6px; color: var(--body); margin-bottom: 14px; white-space: nowrap; }

  .deco-right { position: absolute; left: 891px; top: 499px; width: 140px; height: 173px;
    background: linear-gradient(180deg, #6cc6f5 0%, #3a86c0 60%, var(--deep-navy) 100%); }
  .deco-left { position: absolute; left: 84px; top: 737px; width: 110px; height: 112px; background: var(--amber); }

  .video-shadow { position: absolute; left: 150px; top: 880px; width: 830px; height: 200px;
    background: radial-gradient(ellipse at center top, rgba(0,0,0,0.22), rgba(0,0,0,0) 70%); }
  .video-frame { position: absolute; left: 194px; top: 564px; width: 740px; height: 395px; overflow: hidden;
    background: linear-gradient(180deg, #4a5a7a 0%, #c7d0dc 28%, #dfe4ea 40%, #8d9aae 60%, #5d6a78 80%, #3e4852 100%); }
  .video-caption { position: absolute; left: 326px; top: 195px; width: 351px; height: 84px; background: var(--overlay);
    padding: 11px 0 0 15px; color: #ffffff; font-family: 'Arimo', sans-serif; font-size: 18px; line-height: 22px; white-space: nowrap; }
  .video-caption .muted { color: rgba(255,255,255,0.55); }
  .play-button { position: absolute; left: 337px; top: 176px; width: 68px; height: 68px; border-radius: 50%; background: rgba(40,40,45,0.85); }
  .play-button::after { content: ""; position: absolute; left: 27px; top: 22px; border-left: 20px solid #fff; border-top: 12px solid transparent; border-bottom: 12px solid transparent; }

  .site-footer { position: absolute; left: 84px; right: 83px; top: 1097px; border-top: 1px solid var(--rule); font-family: 'Arimo', sans-serif; }
  .footer-links { position: absolute; left: 0; top: 32px; display: flex; gap: 17px; font-size: 16px; line-height: 20px; color: var(--ink); white-space: nowrap; }
  .footer-links a { color: var(--ink); text-decoration: none; }
  .company-note { position: absolute; left: 0; top: 56px; font-size: 12.5px; line-height: 16px; white-space: nowrap; }
  .social { position: absolute; right: 0; top: 47px; display: flex; gap: 19px; }
  .social span { width: 20px; height: 20px; border-radius: 50%; background: var(--ink); display: block; }
</style>
</head>
<body>
  <header class="site-header">
    <div class="brand">terravane.</div>
    <nav class="main-nav">
      <a href="#">Home</a>
      <a href="#">About Us</a>
      <a href="#">Work</a>
      <a href="#">Contact Us</a>
    </nav>
  </header>

  <section class="about">
    <h1>About</h1>
    <p>We fulfil international property developments in a truly unique way.<br>We’ve worked on projects around the world taking developments from<br>fields to award winning resorts, and tired underachieving developments<br>to overachieving goliaths.</p>
    <p>By creating a unique and bespoke in-house white-label strategy that<br>allows each project to be the only beneficiary of the work we do.</p>
  </section>

  <div class="deco-right" role="img" aria-label="Decorative geometric accent in sky blue and navy"></div>
  <div class="deco-left" role="img" aria-label="Decorative curved accent in amber"></div>

  <div class="video-shadow"></div>
  <div class="video-frame" role="img" aria-label="Video still: dense city skyline of high-rise towers under a hazy sky">
    <div class="video-caption"><span class="muted">is a proven</span> consultancy specialising<br><span class="muted">in the fulfilment of</span> international property<br>developments<span class="muted">.</span></div>
    <div class="play-button"></div>
  </div>

  <footer class="site-footer">
    <div class="footer-links">
      <span>© 2020 Terravane.</span>
      <a href="#">Privacy</a>
      <a href="#">Terms of use</a>
    </div>
    <div class="company-note">A private limited company incorporated in England and Wales under company number 1234567</div>
    <div class="social">
      <span aria-label="Social link"></span>
      <span aria-label="Social link"></span>
      <span aria-label="Social link"></span>
    </div>
  </footer>
</body>
</html>
```